Bright Reed Acupuncture Studio Website Design

We are working with Bright Reed Acunpuncture Studio. They are a local Chinese medicine and acupuncture studio and in need of a new website design.

Some sites to use for inspiration:

https://marblecoveacupuncture.example
https://steadfernacupuncture.example
https://quietharborclinic.example
https://emberdawnacupuncture.example
https://cedarbrookclinic.example

Thank you for taking the time to consider designing a website for us. We are web developers based in Stockton, CA, USA. Most of our projects go through the same process. Understanding this process may help you win a project with us. We custom-code all of our websites in-house. We don’t have any requirements as to what tools you use for your design, but we prefer Figma files. For any design that we label as four-stars, we send it to the client for review. The client picks the final design they want us to use. Once we complete this process, we will continue to show additional clients all the four-star sites and purchase them later. Your designs will have multiple chances to sell. For better chances of success, we ask that you follow these guidelines.

IMAGES:
If you use any images or icons in the design, we ask that you have a link to the asset so we can purchase the image/icon. Most of the designs we submit do not have the customer’s images on them unless they have some great images. Be creative; show us the feeling you are trying to portray with your image choices. Use any royalty-free site you choose. We subscribe to Adobe and mainly use their images, but we can purchase images outside of Adobe.

PLEASE NOTE: we will not submit designs to clients with watermarks on the images.

FONTS:
We ask that you identify the fonts used in the design. This can be done in a message if you want. We typically use Google Fonts and Adobe Fonts.

CONTENT:
We're always open to different content and ideas. We often submit designs with stock images so the client can see our vision. We typically take pictures after the website launch to use their images with our vision. Lorem Ipsum is fine for paragraphs, but we ask that you write the headers in correct English. We want to be able to show the vision and identify the sections of the website.

INSPIRATION:
We typically add a couple of links in the brief of websites we like to help you get started in your design.

REVISIONS:
We do not often ask for revisions of the designs unless we see something in the design that may not appeal to the client. If there are slight changes that we want to make, we do that in the development process.

FEEDBACK:
We rarely give feedback on designs during the design process. We are working on many website projects and do not have the time to provide feedback. We usually respond if your request is well thought out and asks specific questions, but a note asking “feedback, please” usually goes unanswered.

```html
<!DOCTYPE html>
<html lang="en">
<head>
<meta charset="utf-8">
<title>Bright Reed Acupuncture Studio – Home</title>
<link rel="stylesheet" href="https://fonts.googleapis.com/css2?family=Poppins:wght@300;400;500;600;700;800&display=swap">
<style>
  :root{
    --coral:#e06862;
    --coral-soft:#fbe4e3;
    --ink:#111111;
    --black:#000000;
    --white:#ffffff;
    --stage:#e4e4e4;
    --muted:#555555;
  }
  *{box-sizing:border-box;margin:0;padding:0}
  html,body{width:1187px;height:1200px;overflow:hidden}
  body{background:var(--stage);font-family:"Poppins",sans-serif;color:var(--ink);position:relative}
  .page{position:absolute;left:390px;top:20px;width:577px;height:1644px;background:var(--white);
    transform:scale(0.705);transform-origin:top left;overflow:hidden}
  .abs{position:absolute}

  /* hero */
  .hero{position:absolute;left:0;top:0;width:577px;height:256px}
  .hero-photo{position:absolute;inset:0;background:linear-gradient(100deg,#eeeced 0%,#ebe6e6 45%,#d9a88f 68%,#c98a6e 85%,#b7775e 100%)}
  .brand{position:absolute;display:flex;align-items:center;gap:5px;font-weight:600;color:var(--ink)}
  .brand-dot{width:12px;height:12px;border-radius:50%;background:var(--coral)}
  .hero .brand{left:38px;top:16px;font-size:13px}
  .nav{position:absolute;left:171px;top:19px;display:flex;gap:12px;font-size:7px;color:var(--ink)}
  .nav span.drop::after{content:" ⌄"}
  .hero-mark{position:absolute;left:6px;top:124px;font-size:26px;font-weight:700;color:var(--ink);line-height:1}
  .headline{position:absolute;left:184px;top:68px;line-height:1.05}
  .headline b{display:block;font-size:26px;font-weight:700;letter-spacing:-0.5px}
  .headline i{display:block;font-style:normal;font-size:21px;font-weight:300;margin-top:2px}
  .hero-sub{position:absolute;left:185px;top:160px;width:130px;font-size:7px;line-height:1.4}
  .btn{position:absolute;left:184px;top:192px;width:107px;height:23px;border-radius:5px;background:var(--coral);
    color:var(--white);font-size:7px;display:flex;align-items:center;justify-content:center}

  /* about */
  .about{position:absolute;left:0;top:256px;width:577px;height:284px;background:var(--coral);color:var(--white);text-align:center}
  .about-title{position:absolute;left:0;right:0;top:12px;font-size:76px;font-weight:500;letter-spacing:-2px;
    color:transparent;-webkit-text-stroke:1.3px var(--white);line-height:1.1}
  .about-copy{position:absolute;left:80px;right:80px;top:104px;font-size:13.5px;line-height:1.5}
  .about-icon{position:absolute;left:260px;top:186px}

  /* conditions */
  .conditions-title{position:absolute;left:0;right:0;top:602px;text-align:center;font-size:27px;font-weight:700;letter-spacing:-0.5px}
  .arrow-btn{position:absolute;top:607px}
  .card{position:absolute;border-radius:14px;overflow:hidden}
  .card h4{position:absolute;left:13px;top:24px;font-size:9px;font-weight:600}
  .card p{position:absolute;left:13px;width:85px;font-size:6px;line-height:1.5;color:var(--muted)}

  /* services */
  .services{position:absolute;left:0;top:1044px;width:577px;height:334px;background:var(--black);color:var(--white)}
  .services h2{position:absolute;left:0;right:0;top:34px;text-align:center;font-size:27px;font-weight:700;letter-spacing:-0.5px}
  .svc-icon{position:absolute;width:52px;height:52px;border-radius:50%;background:var(--coral);display:flex;align-items:center;justify-content:center}
  .svc-text{position:absolute;width:128px}
  .svc-text h5{font-size:9px;font-weight:600;margin-bottom:12px}
  .svc-text p{font-size:6px;line-height:1.5}
  .btn-outline{position:absolute;left:235px;top:274px;width:107px;height:24px;border:1px solid var(--coral);border-radius:5px;
    font-size:7px;display:flex;align-items:center;justify-content:center}

  /* footer */
  .footer{position:absolute;left:0;top:1378px;width:577px;height:266px}
  .footer .brand{left:84px;top:48px;font-size:13px}
  .footer-quote{position:absolute;left:84px;top:92px;width:130px;font-size:6px;line-height:1.6;color:var(--muted)}
  .footer h6{position:absolute;font-size:7px;font-weight:600}
  .footer-links{position:absolute;left:264px;top:78px;font-size:6px;line-height:14px;color:var(--muted)}
  .contact{position:absolute;left:361px;top:78px;font-size:6px;color:var(--muted)}
  .contact div{display:flex;align-items:center;gap:6px;height:15px}
  .divider{position:absolute;left:82px;top:192px;width:414px;height:1px;background:#e3e3e3}
  .copyright{position:absolute;left:82px;top:213px;font-size:6px;color:var(--muted)}
  .socials{position:absolute;left:452px;top:212px;display:flex;gap:6px}
  .socials span{width:10px;height:10px;border-radius:50%;border:1.5px solid var(--coral)}
</style>
</head>
<body>
<main class="page">

  <section class="hero">
    <div class="hero-photo" role="img" aria-label="Photo of a relaxed woman receiving acupuncture needles on her forehead"></div>
    <div class="brand"><span class="brand-dot"></span>Bright Reed</div>
    <nav class="nav"><span>Home</span><span>About Us</span><span class="drop">Services</span><span>Chronic Pain</span><span>Blog</span><span class="drop">Schedule</span></nav>
    <div class="hero-mark">Bright Reed</div>
    <h1 class="headline"><b>Revitalize</b><b>your energy</b><i>flow naturally</i></h1>
    <p class="hero-sub">Sophisticated Serenity through Acupuncture</p>
    <div class="btn">Book an appointment</div>
  </section>

  <section class="about">
    <h2 class="about-title">About</h2>
    <p class="about-copy">Restore balance, restore health with acupuncture healing through the power of acupuncture nurture your body, mind, and spirit with acupuncture</p>
    <svg class="about-icon" width="60" height="60" viewBox="0 0 60 60" aria-hidden="true">
      <g stroke="#fff" stroke-width="3" stroke-linecap="round">
        <line x1="6" y1="52" x2="30" y2="14"/><line x1="18" y1="56" x2="40" y2="18"/><line x1="30" y1="56" x2="50" y2="20"/>
      </g>
    </svg>
  </section>

  <svg class="arrow-btn" style="left:95px" width="40" height="22" viewBox="0 0 40 22" aria-hidden="true">
    <circle cx="11" cy="11" r="11" fill="var(--coral-soft)"/><path d="M6 11h30M6 11l4-3M6 11l4 3" stroke="#333" stroke-width="1" fill="none"/>
  </svg>
  <h2 class="conditions-title">Conditions We Treat</h2>
  <svg class="arrow-btn" style="left:442px" width="40" height="22" viewBox="0 0 40 22" aria-hidden="true">
    <circle cx="29" cy="11" r="11" fill="var(--coral-soft)"/><path d="M4 11h30M34 11l-4-3M34 11l-4 3" stroke="#333" stroke-width="1" fill="none"/>
  </svg>

  <div class="card" style="left:48px;top:668px;width:234px;height:307px;background:linear-gradient(160deg,#f7efe9 0%,#ece8e6 55%,#e2c8bd 100%)">
    <div class="abs" style="inset:0" role="img" aria-label="Photo of fingers holding fine acupuncture needles"></div>
    <h4>Mental Health</h4><p style="top:50px">24/7 daily support with dignity and independence.</p>
  </div>
  <div class="card" role="img" aria-label="Photo of a woman receiving facial acupuncture" style="left:294px;top:668px;width:112px;height:149px;background:linear-gradient(160deg,#e9d6cc,#caa08a)"></div>
  <div class="card" style="left:416px;top:668px;width:112px;height:149px;background:var(--coral-soft)">
    <h4>Fertility</h4><p style="top:102px">24/7 daily support with dignity and independence.</p>
  </div>
  <div class="card" style="left:294px;top:826px;width:112px;height:149px;background:var(--coral);color:var(--white)">
    <h4>Chronic Pain</h4><p style="top:104px;color:var(--white)">24/7 daily support with dignity and independence.</p>
  </div>
  <div class="card" role="img" aria-label="Photo of a man relaxing with acupuncture needles in his brow" style="left:416px;top:826px;width:112px;height:149px;background:linear-gradient(160deg,#b07a62,#5a3424)"></div>

  <section class="services">
    <h2>Our Services</h2>
    <div class="svc-icon" style="left:98px;top:97px"><svg width="24" height="24" viewBox="0 0 24 24"><path d="M4 20L16 8" stroke="#fff" stroke-width="2" stroke-linecap="round"/><circle cx="17" cy="7" r="3" fill="none" stroke="#fff" stroke-width="2"/></svg></div>
    <div class="svc-text" style="left:160px;top:98px"><h5>Acupuncture</h5><p>We offer personalized assisted living, short-term respite stays, and enriching amenities designed for comfort and wellness.</p></div>
    <div class="svc-icon" style="left:322px;top:97px"><svg width="24" height="24" viewBox="0 0 24 24"><circle cx="12" cy="6" r="3" fill="#fff"/><rect x="9" y="10" width="6" height="11" rx="3" fill="#fff"/></svg></div>
    <div class="svc-text" style="left:385px;top:98px"><h5>Fertility</h5><p>We offer personalized assisted living, short-term respite stays, and enriching amenities designed for comfort and wellness.</p></div>
    <div class="svc-icon" style="left:98px;top:187px"><svg width="26" height="26" viewBox="0 0 26 26"><path d="M3 11h20a10 9 0 0 1-20 0z" fill="#fff"/><rect x="8" y="21" width="10" height="2" fill="#fff"/><line x1="14" y1="10" x2="20" y2="3" stroke="#fff" stroke-width="2.5" stroke-linecap="round"/></svg></div>
    <div class="svc-text" style="left:160px;top:188px"><h5>Nutrition</h5><p>We offer personalized assisted living, short-term respite stays, and enriching amenities designed for comfort and wellness.</p></div>
    <div class="svc-icon" style="left:322px;top:187px"><svg width="26" height="26" viewBox="0 0 26 26"><path d="M5 22L20 5" stroke="#fff" stroke-width="1.5"/><path d="M13 13c-6 0-7-5-7-5s6-1 7 5zM16 10c5 1 6-3 6-3s-5-2-6 3z" fill="#fff"/></svg></div>
    <div class="svc-text" style="left:385px;top:188px"><h5>Herbs</h5><p>We offer personalized assisted living, short-term respite stays, and enriching amenities designed for comfort and wellness.</p></div>
    <div class="btn-outline">View All Services</div>
  </section>

  <footer class="footer">
    <div class="brand"><span class="brand-dot"></span>Bright Reed</div>
    <p class="footer-quote">“Lorem ipsum dolor sit amet, consectetur adipiscing elit. Posuere dignissim aliquam interdum id tincidunti sed vitae elementum sapien. In amet ”</p>
    <h6 style="left:264px;top:60px">Menu</h6>
    <div class="footer-links">Home<br>About Us<br>Services<br>Chronic Pain<br>Blog<br>Schedule</div>
    <h6 style="left:361px;top:60px">Address</h6>
    <div class="contact">
      <div><svg width="8" height="8" viewBox="0 0 10 10"><path d="M5 0a3.5 3.5 0 0 1 3.5 3.5C8.5 6 5 10 5 10S1.5 6 1.5 3.5A3.5 3.5 0 0 1 5 0z" fill="var(--coral)"/></svg>418 Larkspur Way, Milton, TX 75000</div>
      <div><svg width="8" height="8" viewBox="0 0 10 10"><path d="M2 0l2 2-1 2 3 3 2-1 2 2-2 2C4 10 0 6 0 2z" fill="var(--coral)"/></svg>+1 (555) 014-2290</div>
      <div><svg width="8" height="8" viewBox="0 0 10 10"><rect y="2" width="10" height="7" fill="var(--coral)"/><path d="M0 2l5 4 5-4" stroke="#fff" fill="none"/></svg>hello@brightreedacupuncture.example</div>
    </div>
    <div class="divider"></div>
    <p class="copyright">Copyright ©2025 Bright Reed Acupuncture Studio. All Rights Reserved.</p>
    <div class="socials"><span></span><span></span><span></span></div>
  </footer>

</main>
</body>
</html>
```